Tamsel Naturopathics business card design

Using the tamsel logo designed, we would like that incorporated into a business card. A colour scheme which works with the logo and lists the following business details:

Lowen Tamsel - Naturopath
Level 1, 57 Orrick Street
Wollongong NSW
(02) 4813 7096
www.lowentamselnaturo.example

We would also like space on the back of the card for next appointment times.

Target Market(s)

Anyone looking to improve their health

Industry/Entity Type

Business

Requirements
Must have
• Tamsel Naturopathics logo, business details.
Nice to have
• Good colour schemes, attractive, eye-catching features that are easy to read.

```html
<!DOCTYPE html>
<html lang="en">
<head>
<meta charset="utf-8">
<title>Tamsel Naturopathics – Business Card</title>
<link href="https://fonts.googleapis.com/css2?family=Open+Sans:wght@400;600&display=swap" rel="stylesheet">
<style>
  :root {
    --backdrop: #262626;
    --card-dark: #0b0b0b;
    --card-mid: #1d1f21;
    --brand-blue: #1f6fb8;
    --name-light: #d6d6d6;
    --name-dark: #8a8a8a;
    --detail: #b9b9b9;
    --divider: #3a3a3a;
  }
  html, body {
    margin: 0;
    width: 1200px;
    height: 1000px;
    overflow: hidden;
    background: var(--backdrop);
  }
  .card {
    position: absolute;
    left: 76px;
    top: 203px;
    width: 1048px;
    height: 600px;
    background:
      radial-gradient(ellipse 55% 60% at 52% 40%, var(--card-mid), var(--card-dark) 75%);
    box-shadow: 0 6px 24px rgba(0,0,0,0.55);
    font-family: "Open Sans", sans-serif;
  }
  .brand {
    position: absolute;
    left: 60px;
    top: 300px;
    width: 410px;
    margin: 0;
    text-align: center;
    font-size: 34px;
    font-weight: 600;
    color: var(--brand-blue);
    letter-spacing: 1px;
  }
  .divider {
    position: absolute;
    left: 564px;
    top: 180px;
    width: 2px;
    height: 260px;
    background: linear-gradient(to bottom, transparent, var(--divider) 30%, var(--divider) 70%, transparent);
  }
  .person {
    position: absolute;
    left: 596px;
    top: 270px;
    margin: 0;
  }
  .person-name {
    display: block;
    font-size: 44px;
    font-weight: 400;
    letter-spacing: -1.5px;
    line-height: 1.1;
    background: linear-gradient(to bottom, var(--name-light), var(--name-dark));
    -webkit-background-clip: text;
    background-clip: text;
    color: transparent;
  }
  .person-role {
    display: block;
    text-align: right;
    font-size: 14px;
    letter-spacing: 1px;
    color: var(--name-dark);
    margin-top: -4px;
  }
  .detail {
    position: absolute;
    left: 646px;
    display: flex;
    gap: 14px;
    align-items: flex-start;
    font-size: 16px;
    line-height: 23px;
    letter-spacing: 1px;
    color: var(--detail);
  }
  .detail svg { margin-top: 4px; flex: none; }
  .detail-address { top: 390px; }
  .detail-phone { top: 456px; }
  .website {
    position: absolute;
    left: 676px;
    top: 543px;
    font-size: 18px;
    letter-spacing: 1px;
    color: var(--detail);
  }
</style>
</head>
<body>
  <section class="card">
    <h1 class="brand">Tamsel Naturopathics</h1>
    <div class="divider"></div>
    <h2 class="person">
      <span class="person-name">Lowen Tamsel</span>
      <span class="person-role">NATUROPATH</span>
    </h2>
    <div class="detail detail-address">
      <svg width="24" height="26" viewBox="0 0 24 26" aria-hidden="true">
        <path d="M12 1a8 8 0 0 0-8 8c0 6 8 15 8 15s8-9 8-15a8 8 0 0 0-8-8zm0 11a3 3 0 1 1 0-6 3 3 0 0 1 0 6z" fill="var(--detail)"/>
      </svg>
      <div>Level 1, 57 Orrick Street<br>Wollongong NSW</div>
    </div>
    <div class="detail detail-phone">
      <svg width="24" height="26" viewBox="0 0 24 26" aria-hidden="true">
        <path d="M2 9c0-3 4-4 10-4s10 1 10 4v2h-5V9H7v2H2z" fill="var(--detail)"/>
        <path d="M6 12h12l2 10H4z" fill="var(--detail)"/>
        <circle cx="12" cy="17" r="3" fill="#111"/>
      </svg>
      <div>Phone:<br>(02) 4813 7096</div>
    </div>
    <div class="website">www.lowentamselnaturo.example</div>
  </section>
</body>
</html>
```